Modern Podcast Marketing Cards - BRAVOKESTRAL

Update: Do "not" include my address, there's no need for this. Please remember this project needs to promote my brand along with the my new Podcast shows tagline. So this is not a traditional business card, it has to look cool enough so people want to hold onto it and not just toss it aside. So obviously "not" an old school boring business card with a ton of business contact info/text. Needs to catch attention and drive my recipients to want to visit the website " bravokestral.net " and/or to download and listen on the apps Tunevale, Weavly, Mondro Spin. Plus would like to drive them to Follow on my social media channels @BRAVOKESTRAL; all while making sure the the design doesn't look cluttered while not being boring.
I've re-designed the logo specifically for the new show though vs what you see when you first visit my website. So the shows logo is also attached which is found on Tunevale, Weavly app, etc. That design is to promote the three domains this brand focused on "Fueling" the followers and listeners with, regarding "Health", "Business", and "Lifestyle". If logos end up on both sides of the card, one should have the version with the three words included of Health, Business, and Lifestyle. The other side should use the blank version of the logo attached which does not have those three words under the BRAVOKESTRAL logo. So I gave you two versions to work with.
**Try and work in my three domains mentioned above and/or the actual tagline for the show/my brand which is "SPARK Your Health, Business, and Lifestyle". You can break it up a little if it will stand out stronger. Remember this is more of a marketing/advertising card vs a boring traditional business card.
Just to note, my profession behind the Podcast Host is my consulting as a Sales, Marketing, and Business Development consultant, But the final design should really show off my Tagline and those three domains to "SPARK Your Health, Business, and Lifestyle!" (without being cluttered)
- again I like it when the flames get ghosted or used as a transparent backdrop. Or you can somehow take a podcast microphone and overlay my logo's flames to wrap around the microphone or have the microphone stand out with "fire fueling it".
Why the three domains focus?
1. Health: because I'm a health nut, adrenaline junkie sports participant, GritLoop coach, and I have a part time nutritional business.
2. Business: because I'm a business consultant specializing in online branding and social media marketing, with 20 years of business experience.
3. Lifestyle: because I do a lot of coaching on life balance, motivational speaking, love to travel, and am always promoting people to balance their lifestyle between business, personal, and fun.

Target Market(s)

Podcasting, Online Branding & Marketing

Industry/Entity Type

Marketing

Contact Information for Business Card

More of a marketing card than a traditional business card, Double-sided, rich bold colors used from my logo's colors. Will consider the clear plastic style too.

Font styles to use
Serif
Sans Serif

Requirements
Must have
• - Drive people to want to visit the website and download/listen to my podcast via the three apps.
• - So use those apps logos somehow from Tunevale Podcast app, Weavly Radio app, and the Mondro Spin app logos.
• - For contact info: My Name, Titles are Chief Intrepid Officer, also include Podcaster for the 2nd title. Contact info should be 1st my email, 2nd my website address without the www; and third my phone.
• Note: reduce clutter and make sure it's not too busy. That's why I'm considering a 2 sided design.
Nice to have
• - Colors should coincide with my logo and primary colors from the logos.
• - Not too much white, at least side should be a gray or blue backdrop
• - I love the style where you take the flames from my logo and ghost or make them transparent on the backdrop for the background on the card.
• - A podcast microphone logo included somehow or set it one fire with my fire from my logo would be cool.
Should not have
• - Do not list my address
• - No single sided cards
• - No crazy stripes or swoosh marks, emphasis is the FIRE so motivate people, and inspire, "to fire them up" with your design.

```html
<!DOCTYPE html>
<html lang="en">
<head>
<meta charset="utf-8">
<title>BRAVOKESTRAL – SPARK Your Health, Business, and Lifestyle</title>
<link rel="stylesheet" href="https://fonts.googleapis.com/css2?family=Open+Sans:ital,wght@0,400;0,700;1,700;1,800&display=swap">
<style>
  :root {
    --ink: #0d0d0d;
    --paper: #ffffff;
    --brand-blue: #34519b;
    --ghost-flame: #dde3e1;
    --flame-dark: #151515;
    --bar-grey: #dfe3e2;
  }
  html, body {
    margin: 0;
    padding: 0;
    overflow: hidden;
    background: var(--paper);
  }
  .card {
    position: relative;
    width: 725px;
    height: 1200px;
    overflow: hidden;
    background: var(--paper);
    font-family: "Open Sans", Arial, sans-serif;
  }
  .flame-backdrop {
    position: absolute;
    inset: 0;
    width: 725px;
    height: 1200px;
  }
  .tagline {
    position: absolute;
    left: 131px;
    top: 112px;
    margin: 0;
    font-size: 47px;
    font-weight: 700;
    font-style: italic;
    line-height: 78px;
    color: var(--ink);
    letter-spacing: -0.3px;
  }
  .tagline .line { display: block; }
  .tagline .spark {
    display: inline-block;
    background: var(--ink);
    color: var(--paper);
    padding: 0 12px 0 14px;
    margin-left: -16px;
    line-height: 66px;
  }
  .tagline .domain { color: var(--brand-blue); }
  .podcast-mic {
    position: absolute;
    left: 284px;
    top: 545px;
    width: 136px;
    height: 250px;
  }
  .follow-tab {
    position: absolute;
    left: 407px;
    top: 1001px;
    width: 283px;
    height: 60px;
    background: var(--brand-blue);
  }
  .follow-bar {
    position: absolute;
    left: 140px;
    top: 1044px;
    width: 550px;
    height: 104px;
    box-sizing: border-box;
    background: var(--brand-blue);
    padding: 12px 10px;
  }
  .follow-bar__inner {
    height: 100%;
    box-sizing: border-box;
    background: var(--bar-grey);
    border: 2px solid #3a3a3a;
    display: flex;
    align-items: center;
    justify-content: space-between;
    padding: 0 14px 0 16px;
  }
  .social-list {
    display: flex;
    gap: 7px;
    margin: 0;
    padding: 0;
    list-style: none;
  }
  .social-list li {
    font-size: 10.5px;
    font-weight: 700;
    color: var(--ink);
  }
  .follow-label {
    font-size: 20px;
    font-weight: 400;
    color: var(--ink);
  }
</style>
</head>
<body>
<main class="card">
  <svg class="flame-backdrop" viewBox="0 0 725 1200" aria-hidden="false">
    <defs>
      <linearGradient id="darkFlameTone" x1="0" y1="0" x2="0" y2="1">
        <stop offset="0" stop-color="#2b2b2b"/>
        <stop offset="1" stop-color="var(--flame-dark)"/>
      </linearGradient>
    </defs>
    <rect role="img" aria-label="Ghosted pale grey tribal flames rising behind the left side of the card"
          x="0" y="420" width="440" height="780" fill="var(--ghost-flame)"/>
    <rect role="img" aria-label="Bold black tribal flames from the show logo rising along the right side"
          x="425" y="405" width="300" height="795" fill="url(#darkFlameTone)"/>
  </svg>

  <h1 class="tagline">
    <span class="line"><span class="spark">SPARK</span> Your <span class="domain">Health</span>,</span>
    <span class="line"><span class="domain">Business</span>,</span>
    <span class="line">and</span>
    <span class="line"><span class="domain">Lifestyle</span>!</span>
  </h1>

  <svg class="podcast-mic" viewBox="0 0 136 250" role="img" aria-label="Podcast microphone">
    <g fill="none" stroke="var(--ink)" stroke-linecap="round" stroke-width="11">
      <path d="M10 48 A80 80 0 0 1 126 48"/>
      <path d="M34 72 A48 48 0 0 1 102 72"/>
      <path d="M22 160 v12 a46 46 0 0 0 92 0 v-12"/>
      <line x1="68" y1="218" x2="68" y2="236"/>
    </g>
    <rect x="42" y="90" width="52" height="118" rx="26" fill="var(--ink)"/>
    <rect x="40" y="234" width="56" height="12" rx="3" fill="var(--ink)"/>
  </svg>

  <div class="follow-tab"></div>
  <footer class="follow-bar">
    <div class="follow-bar__inner">
      <ul class="social-list">
        <li>Kinra</li>
        <li>Chirpo</li>
        <li>Plexa</li>
        <li>Linkra</li>
        <li>Pinmo</li>
        <li>Tumbo</li>
        <li>Vidlo</li>
        <li>Snapra</li>
        <li>Feedo</li>
      </ul>
      <span class="follow-label">Follow us</span>
    </div>
  </footer>
</main>
</body>
</html>
```